MBW Website

I'm looking to design a 1 page website for my email marketing business called 'Inbox Harvest Works.' The business will be designed to attract eCommerce clients in particular.

It will be a very simple website with my picture, a Subscribe area to capture email addresses (and send out lead magnet PDFs), and some basic copy and social media links, nothing fancy!

I will provide the profile picture and all related copy, looking to use the color green and have it fill up the entire screen.

Here's an example of a similar site I really like:

http://prosecraftacademy-example.com/

I'm just looking for the site to provide information about my email marketing services and make a personal connection with the site visitors.

Target Market(s)

eCommerce businesse customers

Industry/Entity Type

Business

Number of Pages Required

1 page

Font styles to use
Sans Serif

Colors
00a990
33b8a4
87cfc6
cfeae6

Requirements
Must have
• Hosted on HostMoor serviers (we can discuss this*)
• Full page layout (no left/right margins)
• Profile picture / Subscribe and Lead Magnet section above the fold
• Ability for me to supply all copy (against white background)
• Friendloop / Chirply / WorkNest social media icons at the bottom
• Footer section with simple text I will provide

```html
<!DOCTYPE html>
<html lang="en">
<head>
<meta charset="utf-8">
<title>Inbox Harvest Works</title>
<link rel="stylesheet" href="https://fonts.googleapis.com/css2?family=Raleway:wght@400;500;700;800&display=swap">
<style>
  :root {
    --teal: #33b8a4;
    --teal-deep: #00a990;
    --ink: #2f3035;
    --button: #37383d;
    --text: #555;
    --muted: #666;
    --rule: #d9d9d9;
    --white: #fff;
  }
  * { box-sizing: border-box; margin: 0; padding: 0; }
  html, body { width: 1200px; height: 1093px; overflow: hidden; }
  body {
    position: relative;
    font-family: "Raleway", sans-serif;
    background: var(--white);
    color: var(--text);
  }
  .hero-band { position: absolute; left: 0; top: 0; width: 1200px; height: 630px; }
  .hero-copy { position: absolute; left: 121px; top: 160px; width: 500px; }
  .hero-title {
    color: var(--white);
    font-weight: 800;
    font-size: 30px;
    line-height: 38px;
    letter-spacing: -0.2px;
    text-transform: uppercase;
  }
  .hero-lead {
    margin-top: 26px;
    color: #e6f6f3;
    font-size: 14.4px;
    line-height: 18.5px;
    width: 460px;
  }
  .subscribe {
    position: absolute; left: 121px; top: 363px;
    width: 485px; height: 68px; display: flex;
  }
  .subscribe-icon {
    width: 64px; height: 100%; background: var(--white);
    border-right: 1px solid #e3e3e3;
    display: flex; align-items: center; justify-content: center;
  }
  .subscribe-input {
    flex: 1; height: 100%; border: 0; padding-left: 20px;
    font-family: inherit; font-size: 18px; color: #aaa; background: var(--white);
    letter-spacing: 0.5px;
  }
  .subscribe-input::placeholder { color: #aaa; }
  .subscribe-button {
    width: 123px; height: 100%; border: 0; background: var(--button);
    color: var(--white); font-family: inherit; font-weight: 500;
    font-size: 16px; letter-spacing: 1px;
  }
  .profile-photo {
    position: absolute; left: 752px; top: 136px; width: 384px; height: 484px;
    border-radius: 160px 160px 0 0;
    background: linear-gradient(180deg, #c9a48c 0%, #b58d77 40%, #5a5a5a 62%, #4c4c4c 100%);
  }
  .reasons-title {
    position: absolute; left: 0; top: 618px; width: 1200px; text-align: center;
    color: var(--ink); font-weight: 800; font-size: 30px; letter-spacing: 2px;
  }
  .reason-tabs {
    position: absolute; top: 692px; left: 0; width: 1200px;
    list-style: none;
  }
  .reason-tab {
    position: absolute; top: 0; transform: translateX(-50%);
    font-size: 19px; color: var(--muted); letter-spacing: 0.6px;
    padding: 0 4px 8px;
  }
  .reason-tab.is-active { color: var(--teal-deep); border-bottom: 1.5px solid var(--teal-deep); }
  .reason-heading {
    position: absolute; top: 770px; left: 0; width: 1200px; text-align: center;
    color: #222; font-size: 19px; font-weight: 500; letter-spacing: 0.8px;
  }
  .reason-body {
    position: absolute; top: 825px; left: 295px; width: 610px; text-align: center;
    font-size: 13.6px; line-height: 22.5px; color: var(--muted);
  }
  .site-footer {
    position: absolute; top: 1016px; left: 0; width: 1200px; height: 77px;
    border-top: 1px solid var(--rule);
  }
  .follow {
    position: absolute; left: 44px; top: 26px; display: flex; align-items: baseline; gap: 14px;
    font-size: 19px; letter-spacing: 1px;
  }
  .follow-label { color: var(--teal-deep); }
  .social-name { color: #555; font-weight: 700; font-size: 18px; letter-spacing: 0; }
  .footer-note {
    position: absolute; right: 58px; top: 26px;
    font-size: 19px; color: var(--muted); letter-spacing: 1px;
  }
</style>
</head>
<body>
  <svg class="hero-band" viewBox="0 0 1200 630" aria-hidden="true">
    <polygon points="0,0 1200,0 1200,624 0,544" fill="var(--teal)"/>
  </svg>

  <header class="hero-copy">
    <h1 class="hero-title">Learn how to write like you speak and sell like hell</h1>
    <p class="hero-lead">Lorem ipsum dolor sit amet, consectetur adipisicing elit, sed do eiusmod tempor incididunt ut labore et dolore magna aliqua. Ut enim ad minim veniam, quis nostrud exercitation ullamco laboris</p>
  </header>

  <form class="subscribe">
    <span class="subscribe-icon">
      <svg width="30" height="22" viewBox="0 0 30 22" aria-hidden="true">
        <rect x="0" y="0" width="30" height="22" rx="2" fill="#c4c4c4"/>
        <polyline points="1,2 15,12 29,2" fill="none" stroke="#fff" stroke-width="2"/>
      </svg>
    </span>
    <input class="subscribe-input" type="email" placeholder="E-mail Address...">
    <button class="subscribe-button" type="button">SEND</button>
  </form>

  <div class="profile-photo" role="img" aria-label="Portrait photo of the business owner in a dark grey t-shirt, arms crossed"></div>

  <h2 class="reasons-title">WHY CHOOSE THIS</h2>
  <ul class="reason-tabs">
    <li class="reason-tab is-active" style="left:390px">Reason 1</li>
    <li class="reason-tab" style="left:530px">Reason 2</li>
    <li class="reason-tab" style="left:668px">Reason 3</li>
    <li class="reason-tab" style="left:808px">Reason 4</li>
  </ul>
  <h3 class="reason-heading">Reason 1</h3>
  <p class="reason-body">Lorem ipsum dolor sit amet, consectetur adipisicing elit, sed do eiusmod tempor incididunt ut labore et dolore magna aliqua. Ut enim ad minim veniam, quis nostrud exercitation ullamco laboris nisi ut aliquip ex ea commodo consequat. Duis aute irure dolor in reprehenderit in voluptate velit esse cillum dolore eu fugiat nulla pariatur. Excepteur sint occaecat cupidatat non proident, sunt in culpa qui officia deserunt mollit anim id est laborum. Sed ut perspiciatis</p>

  <footer class="site-footer">
    <div class="follow">
      <span class="follow-label">Follow on:</span>
      <span class="social-name">Friendloop</span>
      <span class="social-name">Chirply</span>
      <span class="social-name">WorkNest</span>
    </div>
    <p class="footer-note">Additional Footer Information</p>
  </footer>
</body>
</html>
```